Business Card Design needed for logo design project

Our company needs a Business Card Design. Please refer to our original project in the link above.

Industry/Entity Type

Business

```html
<!DOCTYPE html>
<html lang="en">
<head>
<meta charset="UTF-8">
<title>Ivy Lane Suds – Business Card</title>
<link rel="stylesheet" href="https://fonts.googleapis.com/css2?family=Source+Sans+3:wght@400;600;700&display=swap">
<style>
  :root {
    --backdrop: #e9ecef;
    --brand-indigo: #3d3a98;
    --frame-indigo: #4b48a8;
    --mark-violet: #6c5aa3;
    --card-white: #ffffff;
    --ink: #2b2b33;
    --ink-soft: #44444f;
  }
  * { box-sizing: border-box; margin: 0; padding: 0; }
  html, body {
    width: 1200px; height: 900px; overflow: hidden;
    background: var(--backdrop);
    font-family: "Source Sans 3", Arial, sans-serif;
    color: var(--ink);
  }
  .canvas {
    position: relative; width: 1200px; height: 900px;
  }
  .card {
    position: absolute; left: 250px; width: 700px; height: 400px;
    background: var(--card-white);
    box-shadow: 0 6px 18px rgba(0,0,0,0.12);
    overflow: hidden;
  }
  /* Back side */
  .card-back { top: 40px; background: var(--frame-indigo); }
  .card-back .inner-panel {
    position: absolute; inset: 32px 36px;
    background: var(--card-white);
    display: flex; align-items: center; justify-content: center;
  }
  .brand {
    display: flex; align-items: center; gap: 10px;
  }
  .brand-square {
    width: 22px; height: 22px; background: var(--mark-violet);
  }
  .brand-name {
    font-weight: 700; font-size: 20px; color: var(--ink);
  }
  /* Front side */
  .card-front { top: 470px; }
  .band {
    position: absolute; left: 0; right: 0; height: 34px;
    background: var(--brand-indigo);
  }
  .band-top { top: 0; }
  .band-bottom { bottom: 0; }
  .card-front .brand {
    position: absolute; left: 48px; top: 186px;
  }
  .card-front .brand-name { font-size: 18px; }
  .holder {
    position: absolute; left: 370px; top: 78px;
  }
  .holder-name {
    font-size: 36px; font-weight: 600; letter-spacing: 0.5px; line-height: 1;
    color: var(--ink);
  }
  .holder-title {
    margin-top: 6px; font-size: 17px; color: var(--ink-soft);
  }
  .contacts {
    position: absolute; left: 370px; top: 176px;
    list-style: none;
  }
  .contact {
    display: flex; align-items: flex-start; gap: 12px;
    font-size: 14.5px; line-height: 20px; color: var(--ink-soft);
    margin-bottom: 6px;
  }
  .contact svg { flex: none; width: 18px; height: 18px; margin-top: 1px; fill: var(--mark-violet); }
</style>
</head>
<body>
<main class="canvas">
  <section class="card card-back" aria-label="Card back">
    <div class="inner-panel">
      <div class="brand">
        <span class="brand-square"></span>
        <span class="brand-name">Ivy Lane Suds</span>
      </div>
    </div>
  </section>

  <section class="card card-front" aria-label="Card front">
    <div class="band band-top"></div>

    <div class="brand">
      <span class="brand-square"></span>
      <span class="brand-name">Ivy Lane Suds</span>
    </div>

    <div class="holder">
      <h1 class="holder-name">R.T. Hollis</h1>
      <p class="holder-title">Executive Director</p>
    </div>

    <ul class="contacts">
      <li class="contact">
        <svg viewBox="0 0 24 24" aria-hidden="true"><path d="M12 2a7 7 0 0 0-7 7c0 5.2 7 13 7 13s7-7.8 7-13a7 7 0 0 0-7-7zm0 9.5A2.5 2.5 0 1 1 12 6.5a2.5 2.5 0 0 1 0 5z"/></svg>
        <span>House no-18, Ward no-03<br>Elm Row Township, Westmere - 4127</span>
      </li>
      <li class="contact">
        <svg viewBox="0 0 24 24" aria-hidden="true"><path d="M6.6 10.8a15.1 15.1 0 0 0 6.6 6.6l2.2-2.2a1 1 0 0 1 1-.25 11.4 11.4 0 0 0 3.6.57 1 1 0 0 1 1 1V20a1 1 0 0 1-1 1A17 17 0 0 1 3 4a1 1 0 0 1 1-1h3.5a1 1 0 0 1 1 1c0 1.25.2 2.45.57 3.6a1 1 0 0 1-.25 1z"/></svg>
        <span>+44 0161 555 0198</span>
      </li>
      <li class="contact">
        <svg viewBox="0 0 24 24" aria-hidden="true"><path d="M3 5h18a1 1 0 0 1 1 1v12a1 1 0 0 1-1 1H3a1 1 0 0 1-1-1V6a1 1 0 0 1 1-1zm9 7.2L4.2 7v1.9L12 14l7.8-5.1V7z"/></svg>
        <span>hello@ivylanesuds.com</span>
      </li>
      <li class="contact">
        <svg viewBox="0 0 24 24" aria-hidden="true"><path d="M12 2a10 10 0 1 0 0 20 10 10 0 0 0 0-20zm6.9 9h-3a15.6 15.6 0 0 0-1.3-5.6A8 8 0 0 1 18.9 11zM12 4.1c.9 1.2 1.7 3.7 1.9 6.9h-3.8c.2-3.2 1-5.7 1.9-6.9zM9.4 5.4A15.6 15.6 0 0 0 8.1 11h-3a8 8 0 0 1 4.3-5.6zM5.1 13h3a15.6 15.6 0 0 0 1.3 5.6A8 8 0 0 1 5.1 13zm6.9 6.9c-.9-1.2-1.7-3.7-1.9-6.9h3.8c-.2 3.2-1 5.7-1.9 6.9zm2.6-1.3a15.6 15.6 0 0 0 1.3-5.6h3a8 8 0 0 1-4.3 5.6z"/></svg>
        <span>http://www.ivylanesuds.com</span>
      </li>
    </ul>

    <div class="band band-bottom"></div>
  </section>
</main>
</body>
</html>
```